Bramblewick Gardening Services. A6 flyer single sided

Need an A6 flyer designing. Single sided.
I am a gardener.
I do lawn mowing - one-off garden tidy ups or regular fortnightly visits.
All kinds of trees expertly felled, topped or pruned.
Hedge cutting.
Fencing replaced or repaired.
Fully insured.
Access to fully qualified and licenced tree arborist
07724 316048 or 01632 742918.

I have attached my business card and letter head logo.
I'm open to new designs without incorporating any of my artwork.

Industry/Entity Type

Gardener

```html
<!DOCTYPE html>
<html lang="en">
<head>
<meta charset="utf-8">
<title>Bramblewick Gardening Services – Flyer</title>
<link rel="stylesheet" href="https://fonts.googleapis.com/css2?family=Libre+Baskerville:wght@700&display=swap">
<style>
  :root {
    --lawn-light: #74b83a;
    --lawn-mid: #5a9e2c;
    --lawn-dark: #3f7a1d;
    --mower-dark: #2b2b2b;
    --mower-grey: #5a5a5a;
    --mower-red: #c8322c;
    --headline-yellow: #ffeb00;
    --copy-white: #ffffff;
    --band-white: rgba(255, 255, 255, 0.62);
    --ink: #111111;
  }
  html, body {
    margin: 0;
    padding: 0;
    width: 851px;
    height: 1200px;
    overflow: hidden;
    background: #ffffff;
  }
  .flyer {
    position: relative;
    width: 851px;
    height: 1200px;
    overflow: hidden;
    font-family: "Libre Baskerville", "Bookman Old Style", Georgia, serif;
    font-weight: 700;
  }
  .lawn {
    position: absolute;
    inset: 0;
    background: linear-gradient(170deg, var(--lawn-light) 0%, var(--lawn-mid) 55%, var(--lawn-dark) 100%);
  }
  .mower-photo {
    position: absolute;
    left: 0;
    top: 40px;
    width: 410px;
    height: 1100px;
    border-radius: 0 60px 60px 0;
    background:
      radial-gradient(ellipse at 20% 72%, rgba(200, 50, 44, 0.85), rgba(200, 50, 44, 0) 38%),
      linear-gradient(180deg, rgba(43, 43, 43, 0.55) 0%, rgba(43, 43, 43, 0.7) 45%, var(--mower-grey) 70%, var(--mower-dark) 100%);
  }
  .copy {
    position: absolute;
    left: 425px;
    width: 420px;
    text-align: center;
    margin: 0;
    text-shadow: 0 1px 3px rgba(0, 0, 0, 0.25);
  }
  .headline {
    top: 36px;
    color: var(--headline-yellow);
    font-size: 40px;
    line-height: 56px;
    text-transform: uppercase;
  }
  .services {
    top: 196px;
    color: var(--copy-white);
    font-size: 46px;
    line-height: 62px;
  }
  .trees {
    top: 660px;
    color: var(--copy-white);
    font-size: 31px;
    line-height: 43px;
  }
  .hedges {
    top: 798px;
    color: var(--headline-yellow);
    font-size: 48px;
    line-height: 62px;
  }
  .fencing {
    top: 870px;
    color: var(--copy-white);
    font-size: 32px;
    line-height: 43px;
  }
  .contact-band {
    position: absolute;
    left: 0;
    top: 1013px;
    width: 851px;
    height: 157px;
    background: var(--band-white);
  }
  .contact {
    position: absolute;
    left: 0;
    top: 1022px;
    width: 851px;
    text-align: center;
    margin: 0;
    color: var(--ink);
    font-size: 32px;
    line-height: 46px;
  }
</style>
</head>
<body>
  <main class="flyer">
    <div class="lawn"></div>
    <div class="mower-photo" role="img" aria-label="Photograph of a red petrol lawn mower standing on a freshly cut green lawn"></div>

    <h1 class="copy headline">I am a<br>gardener.</h1>

    <p class="copy services">I do lawn<br>mowing -<br>one-off garden<br>tidy ups or<br>regular<br>fortnightly<br>visits.</p>

    <p class="copy trees">All kinds of trees<br>expertly felled, topped<br>or pruned.</p>

    <h2 class="copy hedges">Hedge Cutting</h2>

    <p class="copy fencing">Fencing replaced or<br>repaired. Fully insured.</p>

    <div class="contact-band"></div>
    <p class="contact">Access to fully qualified<br>and licenced tree arborist<br>07724 316048 or 01632 742918</p>
  </main>
</body>
</html>
```